Stage Design Company Business Card

We are looking to step up up our business card design for our team.

We are a Full service Design and Consultation company for Stage and TV with an emphasis in Theatrical Lighting.

We like our materials to be clean and modern with solid colors free of patterns and gradients. Our brand consists of 4 primary colors Purple, Black, Grey, and White. Provided is our Word Mark as well as our Symbol Logo.

We would like our cards to leave an impression beyond the information, show our attention to design and detail, and make our marks an easily recognized feature (together or apart) for our clients.

We need a warm approachable comfortable feel for some clients, and a professional flair for the board member type clients.

Attached are our brand elements, and our existing cards to give a sense of our style and a glipse at the information we provide on our cards.

Target Market(s)

broad client base from church leaders to high school teachers and architects.

Industry/Entity Type

Business

Contact Information for Business Card

We format our phone number with periods not parenthesis or dashes. Information will be edited for each of our team members, and team member specific cards are not part of this scope, but rather a template so to speak.

Font styles to use
Sans Serif

Colors
6b449b
ffffff
000000
333333
aaaaaa

Requirements
Must have
• Wordmark and logo mark present (does not need to exist on the same side of card)
• Brand Colors,
• Name, Phone, Email, Address.
• Unique choices that make someone stop and take a second look
Nice to have
• It would be nice to somehow convey what we DO, as our brand name does not lend itself to this, outside of an obvious tagline though.....
• social media if not crowded. all of our handles match (instagram, twitter, facebook)
Should not have
• "clipart"

```html
<!DOCTYPE html>
<html lang="en">
<head>
<meta charset="utf-8">
<title>Brennan Stage — Business Card</title>
<link rel="stylesheet" href="https://fonts.googleapis.com/css2?family=Montserrat:wght@500&family=Roboto:wght@400;500&display=swap">
<style>
  :root {
    --brand-purple: #6b449b;
    --brand-white: #ffffff;
    --brand-black: #000000;
    --brand-charcoal: #333333;
    --brand-grey: #aaaaaa;
    --plate-grey: #c4c5c8;
    --backdrop: #646c70;
  }
  * { box-sizing: border-box; margin: 0; padding: 0; }
  html, body {
    width: 1200px; height: 900px; overflow: hidden;
    background: var(--backdrop);
    font-family: "Roboto", Arial, sans-serif;
  }
  .canvas {
    width: 1200px; height: 900px;
    display: flex; align-items: center; justify-content: center; gap: 60px;
  }
  .card {
    position: relative;
    width: 500px; height: 286px;
    border-radius: 18px;
    overflow: hidden;
    box-shadow: 0 14px 30px rgba(0,0,0,.3);
  }

  /* Front */
  .card-front {
    background: var(--brand-purple);
    display: flex; align-items: center; justify-content: center;
  }
  .card-front .wordmark {
    font-family: "Montserrat", Arial, sans-serif;
    font-weight: 500;
    font-size: 34px;
    letter-spacing: 12px;
    color: var(--brand-white);
  }

  /* Back */
  .card-back { background: var(--brand-white); }
  .card-back .color-field {
    position: absolute; inset: 0;
    background: var(--brand-purple);
    clip-path: polygon(74% 0, 100% 0, 100% 100%, 38% 100%);
  }
  .card-back .wordmark {
    position: absolute; left: 30px; top: 30px;
    font-family: "Montserrat", Arial, sans-serif;
    font-weight: 500;
    font-size: 20px;
    letter-spacing: 7px;
    color: var(--brand-purple);
  }
  .contact-list {
    position: absolute; left: 30px; bottom: 34px;
    list-style: none;
    display: flex; flex-direction: column; gap: 8px;
  }
  .contact-item {
    display: flex; align-items: center; gap: 8px;
    font-size: 14px; color: var(--brand-black);
  }
  .contact-icon {
    width: 18px; height: 18px;
    background: var(--brand-purple);
    display: flex; align-items: center; justify-content: center;
  }
  .name-plate {
    position: absolute; right: 0; top: 42px;
    width: 200px; height: 64px;
    background: var(--plate-grey);
    clip-path: polygon(8% 0, 100% 0, 100% 100%, 0 100%);
    display: flex; flex-direction: column; align-items: center; justify-content: center;
    color: var(--brand-black);
  }
  .name-plate .person-name { font-size: 20px; font-weight: 400; }
  .name-plate .person-role { font-size: 9px; font-weight: 500; letter-spacing: .5px; margin-top: 2px; }
  .address {
    position: absolute; right: 70px; bottom: 50px;
    font-size: 14px; line-height: 1.3;
    color: var(--brand-white);
    text-align: center;
  }
</style>
</head>
<body>
  <main class="canvas">
    <section class="card card-front" aria-label="Card front">
      <h1 class="wordmark">BRENNAN STAGE</h1>
    </section>

    <section class="card card-back" aria-label="Card back">
      <div class="color-field"></div>
      <p class="wordmark">BRENNAN STAGE</p>

      <ul class="contact-list">
        <li class="contact-item">
          <span class="contact-icon">
            <svg width="12" height="12" viewBox="0 0 24 24" aria-hidden="true"><path fill="#fff" d="M6.6 10.8a15.1 15.1 0 0 0 6.6 6.6l2.2-2.2c.3-.3.7-.4 1-.2 1.1.4 2.3.6 3.6.6.6 0 1 .4 1 1V20c0 .6-.4 1-1 1A17 17 0 0 1 3 4c0-.6.4-1 1-1h3.5c.6 0 1 .4 1 1 0 1.3.2 2.5.6 3.6.1.3 0 .7-.2 1z"/></svg>
          </span>
          555.014.2283
        </li>
        <li class="contact-item">
          <span class="contact-icon">
            <svg width="12" height="12" viewBox="0 0 24 24" aria-hidden="true"><path fill="#fff" d="M3 5h18v14H3zm2 2v.4l7 4.6 7-4.6V7zm0 2.8V17h14V9.8l-7 4.6z"/></svg>
          </span>
          brennan-stage.com
        </li>
      </ul>

      <div class="name-plate">
        <span class="person-name">Owen R Brennan</span>
        <span class="person-role">OWNER</span>
      </div>

      <p class="address">214 E Oak Ave Tempe<br>AZ 85281</p>
    </section>
  </main>
</body>
</html>
```